E-Book-Cover-Design im Stil eines magischen Buches gesucht
Zielgruppe
Zielgruppe: Paganerds (heidnische Klugscheißer), Geisterbegeisterte, Leute, die Bücher von Hembrick oder Lindqvorn lesen, die sich für Magie, Mythologie, Hexerei interessieren.
Aufgabenstellung
Es sollte wie ein magisches Buch aussehen.
Es wäre schön, auf die in der Einladung erwähnte schwarze Kammer anzuspielen, dort hängt über dem Altar das Luft-Tattwa, ein Kreis in luftig-hellem Blau auf schwarzem Grund.
Ansonsten eine Art Rahmen, vielleicht sowas wie magische Siegel, die das gefährliche Buch unter Kontrolle halten.
Es wäre toll, wenn die Schrift, der Name 'Mira Tolvane' und der Titel 'Vom Nebelreich' im Zusammenhang mit dem hellen Kreis ein passendes kalligraphisches Bild ergeben könnten.
Die angefügten Bilder dienen als Orientierungshilfe.
Falls es nach dem ebook eine Printversion gibt, wäre es schön, auf dem ebook-cover-Design aufzubauen.

```html
<!DOCTYPE html>
<html lang="de">
<head>
<meta charset="utf-8">
<title>Vom Nebelreich – Mira Tolvane</title>
<link href="https://fonts.googleapis.com/css2?family=Pirata+One&display=swap" rel="stylesheet">
<style>
  :root {
    --page-bg: #e4e2df;
    --cover-night: #0f2a36;
    --cover-glow: #3d7394;
    --cover-deep: #06141b;
    --hill-black: #050607;
    --frame-silver: #d9dde0;
    --text-white: #f4f4f2;
    --air-light: #c3dcef;
    --air-mid: #8fb6dd;
    --ornament-silver: #b9c0c4;
  }
  html, body {
    margin: 0;
    width: 1200px;
    height: 960px;
    overflow: hidden;
    background: var(--page-bg);
  }
  .book-cover {
    position: absolute;
    left: 320px;
    top: 80px;
    width: 560px;
    height: 800px;
    overflow: hidden;
    background: var(--cover-deep);
    box-shadow: 0 10px 30px rgba(0,0,0,.25);
  }
  .night-scene {
    position: absolute;
    inset: 0;
    background:
      radial-gradient(ellipse 60% 35% at 62% 36%, var(--cover-glow) 0%, rgba(61,115,148,0) 100%),
      linear-gradient(180deg, var(--cover-night) 0%, #1a4257 45%, var(--cover-deep) 60%);
  }
  .cover-art {
    position: absolute;
    inset: 0;
  }
  .ornament {
    position: absolute;
    width: 36px;
    height: 56px;
    background: var(--cover-night);
    display: flex;
    align-items: center;
    justify-content: center;
  }
  .ornament::after {
    content: "";
    width: 26px;
    height: 44px;
    border-radius: 40%;
    background: radial-gradient(circle, rgba(185,192,196,.55), rgba(185,192,196,.1));
  }
  .ornament--left { left: 12px; top: 318px; background: #13313f; }
  .ornament--right { right: 12px; top: 470px; background: #07161d; }
  .cover-title {
    position: absolute;
    left: 150px;
    top: 140px;
    margin: 0;
    font-family: "Pirata One", "UnifrakturCook", serif;
    font-weight: 400;
    font-size: 96px;
    line-height: .82;
    color: var(--text-white);
    letter-spacing: 1px;
  }
  .cover-title span { display: block; }
  .cover-title .title-line-2 { margin-left: -10px; }
  .cover-author {
    position: absolute;
    left: 0;
    right: 0;
    top: 676px;
    margin: 0;
    text-align: center;
    font-family: "Pirata One", "UnifrakturCook", serif;
    font-weight: 400;
    font-size: 40px;
    color: var(--text-white);
    letter-spacing: 1px;
  }
</style>
</head>
<body>
  <main class="book-cover">
    <div class="night-scene" role="img" aria-label="Kahler, verzweigter Baum vor nebligem, blau leuchtendem Nachthimmel"></div>

    <svg class="cover-art" width="560" height="800" viewBox="0 0 560 800" aria-hidden="true">
      <defs>
        <linearGradient id="airTattwa" x1="0" y1="0" x2="1" y2="1">
          <stop offset="0" stop-color="var(--air-light)"/>
          <stop offset="1" stop-color="var(--air-mid)"/>
        </linearGradient>
      </defs>
      <path class="hill" d="M0 470 C120 430 230 415 330 430 C420 445 500 470 560 455 L560 800 L0 800 Z" fill="var(--hill-black)"/>
      <g class="frame" fill="none" stroke="var(--frame-silver)">
        <path stroke-width="2.5" d="M38 22 H522 A16 16 0 0 0 538 38 V762 A16 16 0 0 0 522 778 H38 A16 16 0 0 0 22 762 V38 A16 16 0 0 0 38 22 Z"/>
        <path stroke-width="1.5" d="M42 30 H518 A12 12 0 0 0 530 42 V758 A12 12 0 0 0 518 770 H42 A12 12 0 0 0 30 758 V42 A12 12 0 0 0 42 30 Z"/>
      </g>
      <g class="air-tattwa">
        <circle cx="280" cy="462" r="104" fill="var(--frame-silver)"/>
        <circle cx="280" cy="462" r="99" fill="var(--hill-black)"/>
        <circle cx="280" cy="462" r="84" fill="url(#airTattwa)"/>
      </g>
    </svg>

    <div class="ornament ornament--left" role="img" aria-label="Silbernes Zierornament"></div>
    <div class="ornament ornament--right" role="img" aria-label="Silbernes Zierornament"></div>

    <h1 class="cover-title"><span class="title-line-1">Vom</span><span class="title-line-2">Nebelreich</span></h1>
    <p class="cover-author">Mira Tolvane</p>
  </main>
</body>
</html>
```